Tamsel Naturopathics business card design

Using the tamsel logo designed, we would like that incorporated into a business card. A colour scheme which works with the logo and lists the following business details:

Lowen Tamsel - Naturopath
Level 1, 57 Orrick Street
Wollongong NSW
(02) 4813 7096
www.lowentamselnaturo.example

We would also like space on the back of the card for next appointment times.

Target Market(s)

Anyone looking to improve their health

Industry/Entity Type

Business

Requirements
Must have
• Tamsel Naturopathics logo, business details.
Nice to have
• Good colour schemes, attractive, eye-catching features that are easy to read.

```html
<!DOCTYPE html>
<html lang="en">
<head>
<meta charset="utf-8">
<title>Tamsel Naturopathics – Business Card</title>
<link rel="stylesheet" href="https://fonts.googleapis.com/css2?family=Jost:wght@400;500;600&family=Arimo:ital@1&display=swap">
<style>
  :root {
    --ink: #231f20;
    --brand-blue: #1f5fa0;
    --sky: #29a9e0;
    --sun: #f2e93a;
    --card-edge: #b9b9b9;
    --paper: #ffffff;
    --label: #111111;
  }
  * { box-sizing: border-box; margin: 0; padding: 0; }
  html, body { width: 1144px; height: 1200px; overflow: hidden; background: var(--paper); }
  body { position: relative; font-family: "Jost", sans-serif; color: var(--ink); }

  .card {
    position: absolute; left: 8px; width: 890px; height: 543px;
    border: 1px solid var(--card-edge); background: var(--paper); overflow: hidden;
  }
  .card--front { top: 8px; }
  .card--back { top: 651px; }

  .side-label {
    position: absolute; left: 1033px;
    font-family: "Arimo", sans-serif; font-style: italic; font-size: 28px; color: var(--label);
  }
  .side-label--front { top: 280px; }
  .side-label--back { top: 915px; }

  /* Front */
  .holder { position: absolute; left: 390px; top: 58px; }
  .holder__name { font-size: 33px; font-weight: 600; line-height: 1; }
  .holder__role { font-size: 30px; font-weight: 400; line-height: 1; margin-top: 8px; }

  .contact { position: absolute; left: 390px; top: 158px; font-size: 21.5px; line-height: 27.5px; list-style: none; }
  .contact__item { display: flex; margin-bottom: 7px; }
  .contact__key { width: 39px; font-weight: 600; font-style: italic; }

  .brand-name {
    position: absolute; left: 58px; top: 445px;
    display: flex; align-items: center; gap: 10px;
    font-size: 24px; font-weight: 500; color: var(--brand-blue); letter-spacing: 0.5px;
  }
  .brand-name__dot { width: 16px; height: 16px; border-radius: 50%; background: var(--sky); }

  /* Back */
  .appt__title {
    position: absolute; left: 46px; top: 58px;
    font-size: 33px; font-weight: 600; color: var(--brand-blue); letter-spacing: 1.5px;
  }
  .days { position: absolute; left: 46px; top: 140px; display: flex; gap: 26px; font-size: 19px; letter-spacing: 1px; }
  .day { display: flex; align-items: center; gap: 7px; }
  .day__box { width: 12px; height: 12px; border: 1.5px solid var(--ink); box-shadow: 2px 2px 0 var(--ink); }

  .field { position: absolute; left: 46px; display: flex; align-items: flex-end; font-size: 18px; letter-spacing: 1px; }
  .field--date { top: 234px; }
  .field--time { top: 293px; }
  .field__label { width: 69px; }
  .field__line { width: 290px; border-bottom: 1px solid var(--ink); height: 16px; margin-bottom: 4px; }

  .reschedule { position: absolute; left: 46px; top: 429px; font-size: 21.5px; }
  .footer-name { position: absolute; left: 46px; top: 475px; font-size: 15px; letter-spacing: 2px; }

  .emblem-area {
    position: absolute; left: 497px; top: 158px; width: 393px; height: 336px;
    background: radial-gradient(circle at 60% 55%, var(--sun) 0%, #9fd6a0 45%, var(--sky) 100%);
    opacity: 0.8;
    clip-path: polygon(0% 6.75%, 20.7% 4.25%, 48.4% 8%, 63.3% 5.5%, 100% 0%, 100% 100%, 48.4% 100%, 48.4% 70.5%, 33.5% 58%, 20.7% 38%, 7.9% 23%);
  }
</style>
</head>
<body>

<section class="card card--front">
  <div class="holder">
    <p class="holder__name">Lowen TAMSEL</p>
    <p class="holder__role">Naturopath</p>
  </div>
  <ul class="contact">
    <li class="contact__item"><span class="contact__key">a</span><span>The Harbourside Wellness and Vitality Centre<br>Level 1, 57 Orrick Street<br>Wollongong NSW 2500</span></li>
    <li class="contact__item"><span class="contact__key">t</span><span>(02) 4813 7096</span></li>
    <li class="contact__item"><span class="contact__key">e</span><span>lowen@lowentamselnaturo.example</span></li>
    <li class="contact__item"><span class="contact__key">w</span><span>www.lowentamselnaturo.example</span></li>
  </ul>
  <div class="brand-name"><span class="brand-name__dot"></span>Tamsel Naturopathics</div>
</section>
<p class="side-label side-label--front">FRONT</p>

<section class="card card--back">
  <h1 class="appt__title">YOUR NEXT APPOINTMENT</h1>
  <div class="days">
    <span class="day">MON<span class="day__box"></span></span>
    <span class="day">TUE<span class="day__box"></span></span>
    <span class="day">WED<span class="day__box"></span></span>
    <span class="day">THURS<span class="day__box"></span></span>
    <span class="day">FRI<span class="day__box"></span></span>
  </div>
  <div class="field field--date"><span class="field__label">Date:</span><span class="field__line"></span></div>
  <div class="field field--time"><span class="field__label">Time:</span><span class="field__line"></span></div>
  <div class="emblem-area" role="img" aria-label="Large decorative brand emblem in blue and yellow gradient"></div>
  <p class="reschedule">Please call (02) 4813 7096 to re-schedule or cancel</p>
  <p class="footer-name">TAMSEL NATUROPATHICS</p>
</section>
<p class="side-label side-label--back">BACK</p>

</body>
</html>
```